Business Card Design

Electronic Security Installation Specialists

Check out our website at www.bramblecoastllc.com to see what we do.

Industry/Entity Type

Business

Contact Information for Business Card

Fern Ridge
Marisol Penton
318 Calloway Drive
Millbrooke, OH 43012

Colors
3176b5
0455a3
ffffff

```html
<!DOCTYPE html>
<html lang="en">
<head>
<meta charset="utf-8">
<title>Fern Ridge – Business Card</title>
<link href="https://fonts.googleapis.com/css2?family=Questrial&family=Ubuntu:wght@500;700&display=swap" rel="stylesheet">
<style>
  :root {
    --page-bg: #e9eaec;
    --navy-dark: #1c3470;
    --navy: #243f86;
    --brand-blue: #0455a3;
    --brand-light: #3176b5;
    --white: #ffffff;
    --silver-light: #f4f4f4;
    --silver-mid: #d9d9d9;
    --silver-dark: #bdbdbd;
    --ink: #1a1a1a;
  }
  * { box-sizing: border-box; margin: 0; padding: 0; }
  html, body {
    width: 1200px; height: 900px; overflow: hidden;
    background: var(--page-bg);
  }
  .stage {
    width: 1200px; height: 900px;
    display: flex; flex-direction: column;
    align-items: center; justify-content: center; gap: 60px;
  }
  .card {
    width: 525px; height: 300px;
    position: relative;
    box-shadow: 0 8px 22px rgba(0,0,0,0.22);
  }
  .card--front {
    background:
      repeating-linear-gradient(0deg, rgba(255,255,255,0.025) 0 1px, transparent 1px 3px),
      linear-gradient(160deg, var(--navy) 0%, var(--navy-dark) 100%);
    display: flex; align-items: center; justify-content: center;
  }
  .brand {
    display: flex; align-items: center; gap: 14px;
    font-family: "Ubuntu", sans-serif; font-weight: 500;
  }
  .brand__dot { width: 22px; height: 22px; border-radius: 50%; }
  .card--front .brand { color: var(--white); font-size: 38px; }
  .card--front .brand__dot { background: var(--white); }
  .card--back {
    background:
      repeating-linear-gradient(0deg, rgba(0,0,0,0.035) 0 1px, transparent 1px 3px),
      linear-gradient(150deg, var(--silver-light) 0%, var(--silver-mid) 55%, var(--silver-dark) 100%);
  }
  .card--back .brand {
    position: absolute; left: 38px; top: 92px;
    color: var(--brand-blue); font-size: 30px;
  }
  .card--back .brand__dot { background: var(--brand-blue); width: 18px; height: 18px; }
  .divider {
    position: absolute; left: 300px; top: 62px;
    width: 2px; height: 102px; background: var(--ink);
  }
  .person-name {
    position: absolute; left: 330px; top: 78px;
    font-family: "Ubuntu", sans-serif; font-weight: 700;
    font-size: 17px; color: var(--ink);
  }
  .address {
    position: absolute; left: 0; right: 0; bottom: 42px;
    text-align: center;
    font-family: "Questrial", sans-serif; font-size: 15px; color: var(--ink);
  }
</style>
</head>
<body>
  <main class="stage">
    <section class="card card--front" aria-label="Card front">
      <div class="brand"><span class="brand__dot"></span><span class="brand__name">Fern Ridge</span></div>
    </section>
    <section class="card card--back" aria-label="Card back">
      <div class="brand"><span class="brand__dot"></span><span class="brand__name">Fern Ridge</span></div>
      <div class="divider"></div>
      <p class="person-name">Marisol Penton</p>
      <p class="address">318 Calloway Drive Millbrooke, OH 43012</p>
    </section>
  </main>
</body>
</html>
```